Campus Parcel Branded Product Information Posters

We need a series of posters designed to promote Campus Parcel's special offers on products that will be available to University Students through the August/September/October period of 2016.

These posters will advertise:
1. "Refer 10 Friends and Get a Free Slatebook Breeze 2"
2. "Earn Money while you're at University as A CP Rep"
3. Promotional Poster of the Vornic QL2840 Featured by Campus Parcel

A Generic Campus Parcel 'template poster' which can be customised to feature different products and product information:
- Vornic RM418 featured by Campus Parcel
- QL9352 featured by Campus Parcel
- Vornic QL6074 featured by Campus Parcel

Photos of all products have been included

I have included the Logo in several sizes and formats, as well as some examples of posters for our current work with Pellor.

Target Market(s)

University Students and Educational Establishments

Industry/Entity Type

Information Technology

Font styles to use
Serif
Sans Serif

Colors
0355a3
3176b5
33a6d7
85cae6
cee9f5
ecf7fa
ffffff
85abd2
86cfc6

Requirements
Must have
• A template which can provide inter-changeability of products and product details.
Nice to have
• Branding consistent with the example designs submitted, contact details for Campus Parcel

```html
<!DOCTYPE html>
<html lang="en">
<head>
<meta charset="utf-8">
<title>Campus Parcel – Rep Poster</title>
<link href="https://fonts.googleapis.com/css2?family=Oswald:wght@400;500&family=Roboto:wght@400&display=swap" rel="stylesheet">
<style>
  :root{
    --sky:#33a6d7;
    --sky-deep:#35a4d8;
    --teal:#4ecac6;
    --navy:#3f5f9e;
    --red:#c00000;
    --ink:#111111;
    --white:#ffffff;
    --mist:#e3ecf5;
    --stage:#2a2a2a;
  }
  html,body{margin:0;padding:0;width:1200px;height:1200px;overflow:hidden;background:var(--stage);}
  .poster-frame{position:absolute;left:189px;top:20px;width:822px;height:1160px;overflow:hidden;}
  .poster{position:absolute;left:0;top:0;width:995px;height:1405px;transform:scale(0.8261);transform-origin:0 0;background:var(--white);overflow:hidden;font-family:'Oswald',sans-serif;}
  .poster > *{position:absolute;}
  .shapes{left:0;top:0;width:995px;height:1405px;}
  .brand-name{left:197px;top:70px;font-family:'Roboto',sans-serif;font-size:42px;color:var(--ink);line-height:1;white-space:nowrap;}
  .offer-title{left:595px;top:40px;font-size:70px;font-weight:500;color:var(--white);line-height:1;letter-spacing:-1px;}
  .sign-text{left:205px;top:352px;width:330px;text-align:center;font-size:86px;font-weight:400;color:var(--teal);line-height:1.15;}
  .headline{left:237px;top:575px;font-size:80px;font-weight:500;color:var(--sky);line-height:1.13;letter-spacing:-1px;white-space:nowrap;}
  .badge-text{left:60px;top:860px;width:360px;text-align:center;color:var(--white);line-height:1;}
  .badge-text .earn{display:block;font-size:118px;font-weight:500;}
  .badge-text .money{display:block;font-size:82px;font-weight:500;margin-top:22px;letter-spacing:-1px;}
  .contact{left:0;top:1278px;width:995px;text-align:center;color:var(--white);font-size:28px;line-height:1.25;}
  .contact .heading{display:block;font-size:27px;}
  .contact .row{display:flex;justify-content:center;gap:110px;}
  .contact .item{display:inline-flex;align-items:center;gap:6px;}
  .contact svg{width:26px;height:26px;fill:var(--white);}
</style>
</head>
<body>
<div class="poster-frame">
  <div class="poster">
    <svg class="shapes" viewBox="0 0 995 1405" xmlns="http://www.w3.org/2000/svg">
      <!-- header -->
      <rect x="0" y="0" width="995" height="18" fill="var(--sky)"/>
      <polygon points="505,18 995,18 995,145 585,145" fill="var(--sky)"/>
      <polygon points="585,145 995,145 995,162 595,162" fill="var(--red)"/>
      <polygon points="0,145 585,145 595,160 0,160" fill="var(--teal)"/>
      <!-- hero photo area -->
      <rect role="img" aria-label="Photo of a smiling student in a green top holding a sign" x="25" y="162" width="970" height="393" fill="url(#heroTone)"/>
      <rect x="205" y="332" width="330" height="225" fill="#e6e6e6"/>
      <!-- logo circle and arc -->
      <path d="M30 160 A 80 80 0 0 0 190 160" fill="none" stroke="var(--teal)" stroke-width="14"/>
      <circle cx="108" cy="100" r="66" fill="var(--ink)" stroke="var(--sky)" stroke-width="4"/>
      <!-- left diagonal bands -->
      <polygon points="0,385 430,1265 0,1265" fill="var(--navy)"/>
      <polygon points="0,590 390,1265 300,1265 0,1030" fill="var(--teal)"/>
      <!-- headline band -->
      <polygon points="120,555 995,555 995,780 235,780" fill="var(--white)"/>
      <polygon points="740,555 995,555 995,780 860,780" fill="var(--mist)" opacity="0.8"/>
      <!-- banknote photo area -->
      <polygon role="img" aria-label="Photo of fanned fifty pound banknotes" points="235,780 995,780 995,1265 430,1265" fill="url(#noteTone)"/>
      <!-- badge -->
      <path d="M240 795 H438 V993 A198 198 0 1 1 240 795 Z" fill="var(--white)"/>
      <path d="M240 817 H416 V993 A176 176 0 1 1 240 817 Z" fill="var(--red)"/>
      <!-- footer -->
      <rect x="0" y="1265" width="995" height="140" fill="var(--sky-deep)"/>
      <defs>
        <linearGradient id="heroTone" x1="0" y1="0" x2="1" y2="0">
          <stop offset="0" stop-color="#f2f3f3"/>
          <stop offset="0.6" stop-color="#e9ece9"/>
          <stop offset="0.75" stop-color="#8fd8a8"/>
          <stop offset="1" stop-color="#eeeeee"/>
        </linearGradient>
        <linearGradient id="noteTone" x1="0" y1="0" x2="1" y2="1">
          <stop offset="0" stop-color="#e8cfd2"/>
          <stop offset="0.5" stop-color="#c9c2c4"/>
          <stop offset="1" stop-color="#9e9a9c"/>
        </linearGradient>
      </defs>
    </svg>

    <div class="brand-name">Campus Parcel</div>
    <div class="offer-title">SPECIAL OFFER</div>
    <div class="sign-text">JOIN<br>US!</div>
    <div class="headline">WHILE YOU'RE AT<br>UNIVERSITY AS A CP REP</div>
    <div class="badge-text"><span class="earn">EARN</span><span class="money">MONEY!</span></div>

    <div class="contact">
      <span class="heading">CONTACT US FOR MORE INFORMATION:</span>
      <div class="row">
        <span class="item"><svg viewBox="0 0 24 24"><path d="M6.6 10.8a15.1 15.1 0 0 0 6.6 6.6l2.2-2.2a1 1 0 0 1 1-.25 11.4 11.4 0 0 0 3.6.57 1 1 0 0 1 1 1V20a1 1 0 0 1-1 1A17 17 0 0 1 3 4a1 1 0 0 1 1-1h3.5a1 1 0 0 1 1 1c0 1.25.2 2.45.57 3.57a1 1 0 0 1-.25 1z"/></svg>Call : 0800 555 0142</span>
        <span class="item"><svg viewBox="0 0 24 24"><path d="M2 5h20v14H2z M2 5l10 8 10-8" fill="none" stroke="#fff" stroke-width="2"/><path d="M2 6l10 8 10-8V5H2z"/></svg>Email : info@campusparcel.co.uk</span>
      </div>
      <span class="item"><svg viewBox="0 0 24 24"><circle cx="12" cy="12" r="10"/><path d="M12 2a15 15 0 0 1 0 20M12 2a15 15 0 0 0 0 20M2 12h20" fill="none" stroke="#35a4d8" stroke-width="1.6"/></svg>www.campusparcel.co.uk</span>
    </div>
  </div>
</div>
</body>
</html>
```